Retro Label for old fashioned soda

We need a label for soda we are having private labeled for our retro, 1950's ice cream shop www.maplewhirlcones.com I don't want the label to look like something from 2017 with a retro feel, but more like an original (possibly kinda cheesy) label you'd see from the 1950's with some of the old catch lines like "tastes great", "invigorating" or "it is refreshing!" The prominent brand should be the name of our ice cream shop, The Maple Whirl. the soda is also pure cane sugar so it might be good to have that on somewhere

Label size is 2.4" wide by 4" tall. Here is an example of some retro labels from findoramap. I attached on file to this contest but there are more here: https://www.findoramap.net/search?q=retro+soda+label

The label will be the same for all the flavors with the exception of the flavor name changing somewhere on the label. These are the flavors

Root Beer
Orange
Black Cherry
Lemonade
Raspberry Lime -Rickey
White Birch Beer
Lemon Iced Tea
Vanilla Cream
Orange Cream
Sarsaparilla
Ginger Ale

Industry/Entity Type

Shop

Colors

Designer to choose colors to be used in the design.

Requirements
Must have
• retro feel. authentic old fashioned look

```html
<!DOCTYPE html>
<html lang="en">
<head>
<meta charset="utf-8">
<title>The Maple Whirl — White Birch Beer Soda Label</title>
<link rel="stylesheet" href="https://fonts.googleapis.com/css2?family=Rubik:wght@700;800;900&family=Yellowtail&family=Josefin+Sans:wght@600;700&family=Kalam:wght@700&display=swap">
<style>
  :root {
    --paper: #f1f1ee;
    --orange: #f0651f;
    --cream: #f4f3dc;
    --lemon: #e6e62a;
    --blue: #2d6fe6;
    --red: #ec4a22;
  }
  html, body {
    margin: 0;
    padding: 0;
    overflow: hidden;
  }
  body {
    width: 911px;
    height: 1200px;
    background: var(--paper);
    position: relative;
  }
  .label-art {
    position: absolute;
    left: 0;
    top: 0;
    width: 911px;
    height: 1200px;
  }
  .label-text {
    position: absolute;
    left: 0;
    width: 911px;
    text-align: center;
    margin: 0;
  }
  .brand-name {
    left: 343px;
    width: 234px;
    top: 398px;
    font-family: "Rubik", sans-serif;
    font-weight: 800;
    font-size: 23px;
    line-height: 28px;
    color: var(--red);
    letter-spacing: 0.5px;
  }
  .flavor-name {
    left: 260px;
    width: 400px;
    top: 535px;
    font-family: "Rubik", sans-serif;
    font-weight: 800;
    font-size: 26px;
    color: var(--cream);
    letter-spacing: 0.3px;
  }
  .flavored {
    left: 260px;
    width: 400px;
    top: 566px;
    font-family: "Yellowtail", cursive;
    font-size: 29px;
    color: var(--blue);
  }
  .soda-word {
    left: 260px;
    width: 400px;
    top: 600px;
    font-family: "Rubik", sans-serif;
    font-weight: 900;
    font-size: 60px;
    line-height: 64px;
    color: var(--red);
    text-shadow: 5px 5px 0 var(--cream);
  }
  .sugar-word {
    left: 410px;
    width: 100px;
    top: 746px;
    font-family: "Josefin Sans", sans-serif;
    font-weight: 700;
    font-size: 25px;
    line-height: 26px;
    color: var(--blue);
    letter-spacing: 1px;
  }
  .sugar-note {
    left: 410px;
    width: 100px;
    top: 773px;
    font-family: "Josefin Sans", sans-serif;
    font-weight: 700;
    font-size: 9.5px;
    color: var(--blue);
    letter-spacing: 0.8px;
  }
  .volume {
    left: 410px;
    width: 100px;
    top: 798px;
    font-family: "Kalam", cursive;
    font-weight: 700;
    font-size: 17px;
    color: var(--red);
  }
</style>
</head>
<body>
  <svg class="label-art" viewBox="0 0 911 1200" xmlns="http://www.w3.org/2000/svg">
    <!-- label body -->
    <rect class="band-top" x="239" y="209" width="451" height="11" fill="var(--orange)"/>
    <rect class="strip-top" x="239" y="220" width="451" height="18" fill="var(--cream)"/>
    <rect class="label-field" x="239" y="238" width="451" height="695" fill="var(--orange)"/>
    <rect class="strip-bottom" x="239" y="933" width="451" height="16" fill="var(--cream)"/>
    <rect class="band-bottom" x="239" y="949" width="451" height="12" fill="var(--orange)"/>

    <!-- cream panel -->
    <path class="cream-panel" fill="var(--cream)"
      d="M317 268 L546 253 Q600 256 616 264 Q640 320 647 387 L656 528 L647 774 Q640 830 616 871 L519 867 L339 876 L328 858 L312 849 Q290 835 282 818 Q266 720 264 616 L268 414 Q276 340 290 290 Z"/>

    <!-- lemon oval -->
    <ellipse class="lemon-oval" cx="460" cy="568" rx="183" ry="280" fill="var(--lemon)"/>

    <!-- name plaque frame -->
    <path class="name-plaque" fill="var(--cream)"
      d="M372 368 Q410 372 440 356 Q452 346 460 340 Q468 346 480 356 Q510 372 548 368 Q554 392 574 404 Q566 432 576 460 Q556 470 548 500 Q508 496 480 512 Q468 520 460 526 Q452 520 440 512 Q412 496 372 500 Q364 470 344 460 Q354 432 346 404 Q366 392 372 368 Z"/>
    <path class="name-plaque-inner" fill="none" stroke="var(--lemon)" stroke-width="3"
      d="M380 378 Q414 380 442 366 Q452 358 460 352 Q468 358 478 366 Q506 380 540 378 Q546 398 562 408 Q556 432 564 456 Q548 466 540 490 Q506 488 478 502 Q468 508 460 514 Q452 508 442 502 Q414 488 380 490 Q374 466 356 456 Q364 432 358 408 Q374 398 380 378 Z"/>

    <!-- bubbles -->
    <g class="bubbles" fill="none" stroke="var(--cream)" stroke-width="3">
      <circle cx="263" cy="282" r="7"/>
      <circle cx="296" cy="267" r="6"/>
      <circle cx="270" cy="263" r="3"/>
      <ellipse cx="619" cy="276" rx="6" ry="10"/>
      <ellipse cx="652" cy="284" rx="8" ry="16" transform="rotate(-20 652 284)"/>
      <ellipse cx="665" cy="359" rx="3" ry="6"/>
      <circle cx="663" cy="786" r="6"/>
      <circle cx="277" cy="897" r="8"/>
    </g>

    <!-- sugar pile -->
    <rect class="sugar-pile" x="422" y="719" width="76" height="26" rx="4" fill="var(--blue)"
      role="img" aria-label="Pile of sugar cubes"/>

    <!-- sugarcane -->
    <rect class="sugarcane" x="514" y="704" width="128" height="176" rx="10" fill="var(--blue)" opacity="0.85"
      role="img" aria-label="Sugarcane stalks growing from a puddle"/>
  </svg>

  <p class="label-text brand-name">THE<br>MAPLE<br>WHIRL</p>
  <p class="label-text flavor-name">WHITE BIRCH BEER</p>
  <p class="label-text flavored">flavored</p>
  <p class="label-text soda-word">SODA</p>
  <p class="label-text sugar-word">SUGAR</p>
  <p class="label-text sugar-note">100% NATURAL</p>
  <p class="label-text volume">XXXml</p>
</body>
</html>
```